Making a tote bag entitled "shopping is hard" *

want to get a simple shopping bag designed with the lettering of "shopping is hard, i want to go do math". need to choose font(s), color(s), as well as any other art that may go around it.

Target Market(s)

studious girls and women, and their supporters

Colors

Designer to choose colors to be used in the design.

```html
<!DOCTYPE html>
<html lang="en">
<head>
<meta charset="UTF-8">
<title>Shopping Is Hard — Tote Bag Print</title>
<link rel="stylesheet" href="https://fonts.googleapis.com/css2?family=Montserrat:wght@300;700&display=swap">
<style>
  :root {
    --bag-white: #ffffff;
    --ink-navy: #1b1e2b;
  }
  html, body {
    margin: 0;
    padding: 0;
    width: 1200px;
    height: 1029px;
    overflow: hidden;
    background: var(--bag-white);
  }
  .bag-face {
    position: relative;
    width: 1200px;
    height: 1029px;
    background: var(--bag-white);
  }
  .slogan {
    position: absolute;
    left: 205px;
    top: 500px;
    margin: 0;
    font-family: "Montserrat", sans-serif;
    font-weight: 300;
    font-size: 78px;
    line-height: 1.28;
    letter-spacing: 0.2px;
    color: var(--ink-navy);
    text-transform: uppercase;
  }
  .slogan .slogan-line {
    display: block;
    white-space: nowrap;
  }
  .slogan strong {
    font-weight: 700;
  }
</style>
</head>
<body>
  <main class="bag-face">
    <p class="slogan">
      <span class="slogan-line"><strong>Shopping</strong> is hard,</span>
      <span class="slogan-line">I want to go</span>
      <span class="slogan-line">do <strong>math</strong>.</span>
    </p>
  </main>
</body>
</html>
```